Startup company business card (Media & Advertising)

we need a business card design for a company that is a startup in the media and aggregation industry. Card needs to look funky and of a new breed/modern and upmarket.

Target Market(s)

advertisers/ brand agencies & media publishers

Industry/Entity Type

Advertising

Contact Information for Business Card

Please ensure the front face signifies our brand (plumvexo.com) and back has details for the contact. Standard contact such as phone , address, email , website etc.

Font styles to use
Other font styles liked:
• use styleguide and logo font and color

Colors

Designer to choose colors to be used in the design.

Requirements
Must have
• We are disrupting the media and agency industry so subtlety would be good to use imagery to signify this
Nice to have
• Please use logo colors for branding
Should not have
• be as creative and provide few options. Pick a brand color from logo and styleguide

```html
<!DOCTYPE html>
<html lang="en">
<head>
<meta charset="utf-8">
<title>plumvexo business card</title>
<link rel="stylesheet" href="https://fonts.googleapis.com/css2?family=Arvo:wght@400;700&display=swap">
<style>
  :root {
    --backdrop: #cdcdcd;
    --card-white: #ffffff;
    --card-black: #0e0e0e;
    --brand-red: #e8333f;
    --brand-red-deep: #b51f3a;
    --ink: #1a1a1a;
    --paper-text: #ffffff;
  }
  * { margin: 0; padding: 0; box-sizing: border-box; }
  html, body {
    width: 1200px;
    height: 802px;
    overflow: hidden;
    background: var(--backdrop);
    font-family: "Arvo", serif;
  }
  .canvas {
    position: relative;
    width: 1200px;
    height: 802px;
  }
  .card {
    position: absolute;
    top: 274px;
    width: 443px;
    height: 264px;
    overflow: hidden;
    box-shadow: 3px 4px 8px rgba(0, 0, 0, 0.35);
  }
  .card--contact { left: 136px; background: var(--card-white); }
  .card--brand { left: 624px; background: var(--card-black); }

  .brand-accent {
    position: absolute;
    left: 215px;
    top: 2px;
    width: 300px;
    height: 300px;
  }

  .person-name {
    position: absolute;
    left: 20px;
    top: 34px;
    font-size: 15px;
    font-weight: 700;
    color: var(--brand-red);
    letter-spacing: 0.1px;
  }
  .person-role {
    position: absolute;
    left: 20px;
    top: 53px;
    font-size: 12px;
    color: var(--ink);
  }
  .contact-list {
    position: absolute;
    left: 20px;
    top: 142px;
    list-style: none;
    font-size: 11.5px;
    color: var(--ink);
  }
  .contact-list li {
    display: flex;
    align-items: center;
    height: 16.5px;
  }
  .contact-icon {
    width: 12px;
    height: 12px;
    margin-right: 2px;
    flex: none;
  }
  .postal-address {
    position: absolute;
    left: 21px;
    top: 200px;
    font-size: 11.5px;
    line-height: 16px;
    font-style: normal;
    color: var(--ink);
  }

  .wordmark {
    position: absolute;
    left: 75px;
    top: 104px;
    display: flex;
    align-items: center;
  }
  .wordmark-dot {
    width: 56px;
    height: 56px;
    border-radius: 50%;
    background: var(--brand-red);
    margin-right: 42px;
  }
  .wordmark-name {
    font-size: 40px;
    font-weight: 700;
    color: var(--paper-text);
    letter-spacing: 0.5px;
  }
</style>
</head>
<body>
<main class="canvas">
  <section class="card card--contact">
    <svg class="brand-accent" viewBox="0 0 300 300" role="img" aria-label="Large red brand accent shape">
      <defs>
        <linearGradient id="accentFill" x1="0" y1="0" x2="1" y2="0">
          <stop offset="0" stop-color="#e8333f"/>
          <stop offset="1" stop-color="#b51f3a"/>
        </linearGradient>
      </defs>
      <circle cx="150" cy="150" r="150" fill="url(#accentFill)"/>
    </svg>

    <h1 class="person-name">Marcus Ellery</h1>
    <p class="person-role">Managing Director</p>

    <ul class="contact-list">
      <li>
        <svg class="contact-icon" viewBox="0 0 12 12" aria-hidden="true">
          <rect x="0.6" y="0.6" width="10.8" height="10.8" rx="1.5" fill="none" stroke="#e8333f" stroke-width="1.1"/>
          <path d="M3.6 2.8c-.5.3-.7 1-.3 2 .6 1.6 1.8 3 3.3 3.8.9.5 1.6.3 1.9-.2l.3-.6-1.3-.9-.6.6c-.9-.4-1.7-1.3-2.1-2.2l.6-.6-.8-1.4z" fill="#e8333f"/>
        </svg>
        061-482 730 215
      </li>
      <li>
        <svg class="contact-icon" viewBox="0 0 12 12" aria-hidden="true">
          <rect x="0.5" y="2.5" width="11" height="7.5" fill="#e8333f"/>
          <path d="M0.5 2.8 6 7 11.5 2.8" fill="none" stroke="#fff" stroke-width="1"/>
        </svg>
        hello@plumvexo.com
      </li>
      <li>
        <svg class="contact-icon" viewBox="0 0 12 12" aria-hidden="true">
          <g fill="none" stroke="#e8333f" stroke-width="1">
            <circle cx="6" cy="6" r="5.2"/>
            <ellipse cx="6" cy="6" rx="2.3" ry="5.2"/>
            <path d="M0.8 6h10.4M1.6 3.4h8.8M1.6 8.6h8.8"/>
          </g>
        </svg>
        www.plumvexo.com
      </li>
    </ul>

    <address class="postal-address">
      87, Harlow Crescent<br>
      Wrenfield, 30917
    </address>
  </section>

  <section class="card card--brand">
    <div class="wordmark">
      <span class="wordmark-dot" aria-hidden="true"></span>
      <span class="wordmark-name">plumvexo</span>
    </div>
  </section>
</main>
</body>
</html>
```